TWD OPRA Thank You card

We need a thank you card to give to our various stakeholders. The card design needs to be professional, corporate, and use elements of our current visual identity (colours and logo will be supplied). The inside of the card needs to have a space for a personal message to be written. Our target card size is 5 x 7.

As a bit of background, we fund local health care in Provincia. We do not directly provide front-line health care services. We do manage the funding and performance monitoring for the agencies we fund. We engage a wide range of people from CEO's, to MPP's, to the general public on a variety of health care topics. At the heart of it, we are a local organization that works to improve health care in Windsor/Essex, Chatham-Kent, and Sarnia/Lambton.

The final design should lean towards a more traditional look.

Industry/Entity Type

It Professional

Requirements
Must have
• It must incorporate our colour pallet and logo

```html
<!DOCTYPE html>
<html lang="en">
<head>
<meta charset="utf-8">
<title>TWD OPRA Thank You Card</title>
<link rel="stylesheet" href="https://fonts.googleapis.com/css2?family=Open+Sans:wght@400;600;700&family=Pinyon+Script&display=swap">
<style>
  :root {
    --plum: #5e0a55;
    --plum-deep: #4d0746;
    --violet: #7f3b8c;
    --orange: #e0781e;
    --orange-light: #f09a3e;
    --gold: #d8c48e;
    --gold-deep: #c2aa70;
    --silver: #a9a9ad;
    --silver-light: #d6d6d8;
    --paper: #ffffff;
    --rule: #9a9a9a;
    --ink-light: #ffffff;
  }
  html, body {
    margin: 0;
    padding: 0;
    width: 861px;
    height: 1200px;
    overflow: hidden;
    background: var(--plum);
  }
  .card {
    position: relative;
    width: 861px;
    height: 1200px;
    overflow: hidden;
    font-family: "Open Sans", Arial, sans-serif;
  }
  .card-art {
    position: absolute;
    inset: 0;
    width: 861px;
    height: 1200px;
    display: block;
  }
  .brand {
    position: absolute;
    left: 150px;
    top: 52px;
    width: 330px;
    color: var(--ink-light);
  }
  .brand-name {
    display: flex;
    align-items: center;
    gap: 16px;
    font-size: 52px;
    font-weight: 400;
    line-height: 1;
    padding-bottom: 8px;
    border-bottom: 2px solid var(--ink-light);
    margin-left: -48px;
    padding-left: 0;
  }
  .brand-mark {
    width: 34px;
    height: 34px;
    border-radius: 50%;
    background: var(--ink-light);
    flex: none;
  }
  .brand-unit {
    margin: 8px 0 0 0;
    font-size: 16px;
    font-weight: 700;
    line-height: 1.2;
    padding-bottom: 6px;
    border-bottom: 1px solid var(--ink-light);
  }
  .brand-unit-fr {
    margin: 6px 0 0 0;
    font-size: 16px;
    font-weight: 700;
    line-height: 1.2;
  }
  .greeting {
    position: absolute;
    right: 40px;
    bottom: 52px;
    margin: 0;
    font-family: "Pinyon Script", "Brush Script MT", cursive;
    font-weight: 400;
    font-size: 84px;
    line-height: 1;
    color: var(--plum);
    transform: rotate(-6deg);
  }
</style>
</head>
<body>
<main class="card">
  <svg class="card-art" viewBox="0 0 861 1200" xmlns="http://www.w3.org/2000/svg" aria-hidden="false">
    <defs>
      <linearGradient id="silver-fill" x1="0" y1="0" x2="1" y2="1">
        <stop offset="0" stop-color="var(--silver)"/>
        <stop offset="0.45" stop-color="var(--silver-light)"/>
        <stop offset="1" stop-color="var(--silver)"/>
      </linearGradient>
      <linearGradient id="orange-fill" x1="0" y1="0" x2="0" y2="1">
        <stop offset="0" stop-color="var(--orange)"/>
        <stop offset="0.6" stop-color="var(--orange-light)"/>
        <stop offset="1" stop-color="var(--orange)"/>
      </linearGradient>
      <linearGradient id="gold-fill" x1="0" y1="0" x2="1" y2="1">
        <stop offset="0" stop-color="var(--gold-deep)"/>
        <stop offset="0.5" stop-color="var(--gold)"/>
        <stop offset="1" stop-color="var(--gold-deep)"/>
      </linearGradient>
      <clipPath id="note-clip">
        <rect x="70" y="420" width="540" height="580" rx="70" transform="rotate(-5 340 710)"/>
      </clipPath>
    </defs>

    <rect class="plum-field" width="861" height="1200" fill="var(--plum)"/>

    <path class="silver-field" fill="url(#silver-fill)"
      d="M0 300 C0 272 22 262 50 266 L430 330 C520 345 560 420 565 520 C570 700 510 920 450 1200 L0 1200 Z"/>

    <path class="violet-ribbon" fill="var(--violet)"
      d="M628 640 C640 820 590 1020 570 1200 L520 1200 C545 1030 605 860 620 690 Z"/>

    <path class="orange-ribbon" fill="url(#orange-fill)"
      d="M575 300 C640 430 650 560 630 700 C605 880 550 1030 525 1200 L470 1200 C500 1040 560 880 585 700 C605 560 605 430 575 300 Z"/>

    <path class="pattern-panel" fill="url(#gold-fill)" role="img"
      aria-label="Ornamental paisley and swirl pattern in soft gold tones"
      d="M575 0 L861 0 L861 1200 L560 1200 C580 1020 640 820 652 620 C665 420 600 200 575 0 Z"/>

    <g class="message-area">
      <rect x="70" y="420" width="540" height="580" rx="70" fill="var(--paper)" transform="rotate(-5 340 710)"/>
      <g class="writing-lines" clip-path="url(#note-clip)" stroke="var(--rule)" stroke-width="1.2" stroke-dasharray="2 3">
        <line x1="40" y1="455" x2="650" y2="455"/>
        <line x1="40" y1="497" x2="650" y2="497"/>
        <line x1="40" y1="539" x2="650" y2="539"/>
        <line x1="40" y1="581" x2="650" y2="581"/>
        <line x1="40" y1="623" x2="650" y2="623"/>
        <line x1="40" y1="665" x2="650" y2="665"/>
        <line x1="40" y1="707" x2="650" y2="707"/>
        <line x1="40" y1="749" x2="650" y2="749"/>
        <line x1="40" y1="791" x2="650" y2="791"/>
        <line x1="40" y1="833" x2="650" y2="833"/>
        <line x1="40" y1="875" x2="650" y2="875"/>
        <line x1="40" y1="917" x2="650" y2="917"/>
        <line x1="40" y1="959" x2="650" y2="959"/>
        <line x1="40" y1="1001" x2="650" y2="1001"/>
      </g>
    </g>
  </svg>

  <header class="brand">
    <div class="brand-name"><span class="brand-mark"></span>Provincia</div>
    <p class="brand-unit">Tri-Water District Health<br>Resource Office</p>
    <p class="brand-unit-fr">Bureau régional des ressources<br>de santé du district<br>Tri-Eaux</p>
  </header>

  <p class="greeting">Thank You</p>
</main>
</body>
</html>
```